A new PowerPoint Template for a French consulting company

Who are we?

Formed in 2005, Quorv is a consulting company specialising in the human aspect of change and transformation.

From our offices in the heart of Paris, our team of 30 consultants work with leading organisations in the Aerospace, Finance, Transportation and Public sectors to deliver lasting change.

Our customers trust us with some of their most strategic and sensitive projects. They trust us with these projects because:
- We listen to them, ensuring we understand the real needs of their business
- We involve them, co-developing and tailoring our solutions to the specific challenges they face
- We’re professional, without taking ourselves too seriously
- We’re imaginative, whilst always remaining pragmatic
- We get results!

You can find out more about who we are and the work we do here: http://www.quorv-example.fr/en

What we need from you?

We’re approaching our 10th birthday and, whilst we still love what we do, we think it’s the right time to update our image.

We’d like you to design us a new PowerPoint template, that will be used for all of our internal and client facing work. You can base your submissions on our existing logo and colour scheme (see files attached) or you can submit your own fresh ideas – after all, we’re not afraid of change!

Finally, whilst we’re looking for you to be creative, there are some simple guidelines that we need you to keep in mind:

1. The Template needs to include both a front cover and a “content” page

2. The front cover needs to:
- Include our logo
- Reflect “who we are” and the type of work that we do

3. The content page needs to:
- Have a predominantly white background
- Be practical to use, making an effective use of the 4:3 standard PPT size
- Include an area across the top of the page for the slide title
- Include areas along the bottom of the page for the page number and date

4. If you decide to propose a new colour scheme, it should be balanced and the “accents” usable

5. The PowerPoint Template needs to be “printer friendly”

6. The fonts you use should be standard

What we don’t want?

To give you as much help as possible, here are some things that we really don’t want:

- Submissions that are dull grey or navy blue, suggesting we’re nothing but boring corporate suits
- Submissions that are Lulette pink or too “soft and cuddly”
- Submissions that use lots of stock images of “happy, smiling, consultants”
- Submissions that will be the height of fashion today, but completely out of date next year

```html
<!DOCTYPE html>
<html lang="en">
<head>
<meta charset="utf-8">
<title>Quorv — Presentation Template</title>
<link rel="stylesheet" href="https://fonts.googleapis.com/css2?family=Lato:ital,wght@0,400;0,700;1,400;1,700&family=Open+Sans:wght@300;400;600;700&display=swap">
<style>
:root{
  --stage:#a3abb0;
  --maroon:#6c0e40;
  --teal:#00b1a6;
  --pink:#d9709e;
  --gold:#f5cf6a;
  --sky:#cfe6f0;
  --paper:#ffffff;
  --band:#f4f4f4;
  --row:#f7f7f7;
  --rule:#e2e2e2;
  --ink:#555555;
  --dark:#343434;
  --dark-rule:#555555;
  --cover:#3b3b3b;
}
*{box-sizing:border-box;margin:0;padding:0}
html,body{width:1200px;height:916px;overflow:hidden;background:var(--stage)}
body{position:relative;font-family:"Open Sans",Arial,sans-serif;color:var(--ink)}

.slide{position:absolute;width:582px;height:436px;background:var(--paper);overflow:hidden}
.slide--tables{left:14px;top:12px}
.slide--graphs{left:606px;top:12px}
.slide--bullets{left:14px;top:464px}
.slide--cover{left:606px;top:464px}

.slide-header{position:absolute;left:0;top:0;width:100%;height:40px;background:var(--band);border-top:2px solid var(--teal)}
.slide-header__texture{position:absolute;right:0;top:0;width:230px;height:38px;background:linear-gradient(90deg,rgba(0,0,0,0),rgba(0,0,0,.035))}
.slide-title{position:absolute;left:16px;top:9px;font-family:"Lato",sans-serif;font-size:20px;font-weight:400;color:var(--maroon);letter-spacing:.3px;white-space:nowrap}
.slide-subtitle{font-size:9px;color:var(--teal);margin-left:10px;letter-spacing:.2px;vertical-align:3px}
.slide-subtitle b{font-weight:700}

.slide-footer{position:absolute;left:0;bottom:0;width:100%;height:37px;background:var(--band)}
.footer-brand{position:absolute;left:16px;top:8px;font-family:"Lato",sans-serif;font-size:18px;font-weight:700;color:var(--maroon)}
.footer-label{position:absolute;left:74px;top:14px;font-size:7.5px;color:var(--teal)}
.footer-label b{font-weight:700}
.page-number{position:absolute;right:18px;top:13px;font-size:8px;font-weight:700;color:var(--teal)}

/* tables */
.theme-heading{position:absolute;top:75px;font-family:"Lato",sans-serif;font-size:15px;font-weight:400;color:#666;display:flex;align-items:center;gap:6px}
.theme-heading b{font-weight:700}
.theme-heading--light{left:24px}
.theme-heading--dark{left:300px}
.plan-table{position:absolute;top:103px;width:260px;border-collapse:collapse;font-size:5.5px}
.plan-table--light{left:22px}
.plan-table--dark{left:302px}
.plan-table th{height:25px;font-size:8.5px;font-weight:400;color:#fff;text-align:center}
.plan-table td{height:25.2px;padding:0 4px;border-bottom:1px solid var(--rule);border-right:1px solid var(--rule)}
.plan-table td:last-child{border-right:0}
.plan-table .col-item{width:34px;text-align:center;font-size:8px}
.plan-table .col-step{width:98px}
.plan-table .col-resp{width:67px}
.plan-table .col-date{text-align:center}
.plan-table tfoot td{height:26px;text-align:center;font-size:8.5px;color:#fff;border:0}
.plan-table--light th{background:var(--maroon);color:#fff}
.plan-table--light td{background:var(--row);color:var(--ink)}
.plan-table--light td.col-item{color:var(--teal)}
.plan-table--light tfoot td{background:var(--teal);color:#fff}
.plan-table--dark th{background:var(--teal)}
.plan-table--dark td{background:var(--dark);color:#fff;border-color:var(--dark-rule)}
.plan-table--dark tfoot td{background:var(--maroon)}

/* graph */
.pyramid{position:absolute;left:0;top:0}
.pyramid text{font-family:"Lato",sans-serif;fill:#fff;text-anchor:middle}
.pyramid .pct{fill:var(--teal);font-size:14px}

/* bullets */
.bullet-list{position:absolute;left:62px;top:126px;width:460px;list-style:none;font-size:8.6px;line-height:13px;color:var(--ink)}
.bullet-list li{position:relative;padding-left:16px;margin-bottom:12.5px}
.bullet-list li::before{content:"";position:absolute;left:0;top:3px;border-left:4px solid var(--teal);border-top:3.5px solid transparent;border-bottom:3.5px solid transparent}
.bullet-list b{font-weight:700;color:#444}

/* cover */
.slide--cover{background:linear-gradient(160deg,#454545,var(--cover) 60%,#333)}
.cover-texture{position:absolute;inset:0;background:linear-gradient(90deg,rgba(255,255,255,.015),rgba(255,255,255,0))}
.cover-brand{position:absolute;left:0;width:100%;top:66px;text-align:center;font-family:"Lato",sans-serif;font-weight:700;font-size:96px;line-height:1;color:#fff;letter-spacing:-1px}
.cover-tagline{position:absolute;left:0;width:100%;top:204px;text-align:center;font-family:"Open Sans",sans-serif;font-weight:300;font-size:27px;color:var(--teal)}
.cover-contact{position:absolute;left:24px;top:330px;font-size:9.5px;line-height:12.5px;color:#fff}
.cover-contact dt{color:var(--teal);font-weight:700}
.cover-contact dd{margin-bottom:10px}
.cover-contact a{color:#fff}
.social-links{position:absolute;right:22px;top:403px;display:flex;gap:10px}
.social-links span{width:11px;height:11px;border-radius:50%;background:var(--teal)}
</style>
</head>
<body>

<section class="slide slide--tables">
  <header class="slide-header">
    <div class="slide-header__texture" role="img" aria-label="faint diagonal line texture"></div>
    <h1 class="slide-title">COLOR STYLE TABLES<span class="slide-subtitle">CHOOSE FROM A <b>LIGHT</b> OR <b>DARK</b> THEME</span></h1>
  </header>

  <h2 class="theme-heading theme-heading--light">
    <svg width="18" height="14" viewBox="0 0 18 14"><rect width="18" height="14" rx="1.5" fill="#00b1a6"/><path d="M1.5 4.5h15M1.5 8.5h15M6.5 1.5v11M11.5 1.5v11" stroke="#fff" stroke-width="1.2"/></svg>
    <span><b>Light</b> Theme</span>
  </h2>
  <table class="plan-table plan-table--light">
    <thead><tr><th class="col-item">Item</th><th class="col-step">Step/Action</th><th class="col-resp">Responsible</th><th class="col-date">Target Date</th></tr></thead>
    <tbody>
      <tr><td class="col-item">1</td><td>Business X,Y, Z high level needs</td><td>Business X,Y, Z</td><td class="col-date">5/24/2013</td></tr>
      <tr><td class="col-item">2</td><td>Understand current situation and safety mana</td><td>Business X,Y, Z</td><td class="col-date">5/31/2013</td></tr>
      <tr><td class="col-item">3</td><td>Submit Proposal</td><td>Business X,Y, Z</td><td class="col-date">6/3/2013</td></tr>
      <tr><td class="col-item">4</td><td>Review Proposal</td><td>Business X,Y, Z</td><td class="col-date">TBD</td></tr>
      <tr><td class="col-item">5</td><td>Prepare Final Proposal &amp; Statement of Work (SOW)</td><td>Business X,Y, Z</td><td class="col-date">TBD</td></tr>
      <tr><td class="col-item">6</td><td>Complete and sign SOW</td><td>Business X,Y, Z</td><td class="col-date">TBD</td></tr>
      <tr><td class="col-item">7</td><td>Schedule project start data</td><td>Business X,Y, Z</td><td class="col-date">TBD</td></tr>
      <tr><td class="col-item">8</td><td>Kick-off Project</td><td>Business X,Y, Z</td><td class="col-date">TBD</td></tr>
      <tr><td class="col-item">9</td><td>Complete Project</td><td>Business X,Y, Z</td><td class="col-date">TBD</td></tr>
    </tbody>
    <tfoot><tr><td colspan="4">* Additional Information</td></tr></tfoot>
  </table>

  <h2 class="theme-heading theme-heading--dark">
    <svg width="18" height="14" viewBox="0 0 18 14"><rect width="18" height="14" rx="1.5" fill="#6c0e40"/><path d="M1.5 4.5h15M1.5 8.5h15M6.5 1.5v11M11.5 1.5v11" stroke="#fff" stroke-width="1.2"/></svg>
    <span><b>Dark</b> Theme</span>
  </h2>
  <table class="plan-table plan-table--dark">
    <thead><tr><th class="col-item">Item</th><th class="col-step">Step/Action</th><th class="col-resp">Responsible</th><th class="col-date">Target Date</th></tr></thead>
    <tbody>
      <tr><td class="col-item">1</td><td>Business X,Y, Z high level needs</td><td>Business X,Y, Z</td><td class="col-date">5/24/2013</td></tr>
      <tr><td class="col-item">2</td><td>Understand current situation and safety mana</td><td>Business X,Y, Z</td><td class="col-date">5/31/2013</td></tr>
      <tr><td class="col-item">3</td><td>Submit Proposal</td><td>Business X,Y, Z</td><td class="col-date">6/3/2013</td></tr>
      <tr><td class="col-item">4</td><td>Review Proposal</td><td>Business X,Y, Z</td><td class="col-date">TBD</td></tr>
      <tr><td class="col-item">5</td><td>Prepare Final Proposal &amp; Statement of Work (SOW)</td><td>Business X,Y, Z</td><td class="col-date">TBD</td></tr>
      <tr><td class="col-item">6</td><td>Complete and sign SOW</td><td>Business X,Y, Z</td><td class="col-date">TBD</td></tr>
      <tr><td class="col-item">7</td><td>Schedule project start data</td><td>Business X,Y, Z</td><td class="col-date">TBD</td></tr>
      <tr><td class="col-item">8</td><td>Kick-off Project</td><td>Business X,Y, Z</td><td class="col-date">TBD</td></tr>
      <tr><td class="col-item">9</td><td>Complete Project</td><td>Business X,Y, Z</td><td class="col-date">TBD</td></tr>
    </tbody>
    <tfoot><tr><td colspan="4">* Additional Information</td></tr></tfoot>
  </table>

  <footer class="slide-footer">
    <span class="footer-brand">Quorv</span>
    <span class="footer-label">| <b>COMPANY</b> PRESENTATION</span>
    <span class="page-number">5</span>
  </footer>
</section>

<section class="slide slide--graphs">
  <header class="slide-header">
    <div class="slide-header__texture" role="img" aria-label="faint diagonal line texture"></div>
    <h1 class="slide-title">STYLE GRAPHS</h1>
  </header>

  <svg class="pyramid" width="582" height="436" viewBox="0 0 582 436">
    <defs>
      <marker id="arrow-head" markerWidth="8" markerHeight="8" refX="6" refY="4" orient="auto">
        <path d="M0 0L7 4L0 8" fill="none" stroke="#f5cf6a" stroke-width="1.4"/>
      </marker>
    </defs>
    <line x1="249" y1="106" x2="124" y2="353" stroke="#cfe6f0" stroke-width="2"/>
    <line x1="344" y1="100" x2="410" y2="224" stroke="#f5cf6a" stroke-width="2" marker-end="url(#arrow-head)"/>

    <polygon points="300,63 316,95 284,95" fill="#d9709e"/>
    <polygon points="281,101 317,101 384,230 217,230" fill="#6c0e40"/>
    <polygon points="207,236 395,236 460,385 140,385" fill="#00b1a6"/>

    <circle cx="256" cy="85" r="21" fill="#fff" stroke="#00b1a6" stroke-width="1.5"/>
    <text class="pct" x="256" y="90">5%</text>
    <circle cx="216" cy="167" r="21" fill="#fff" stroke="#00b1a6" stroke-width="1.5"/>
    <text class="pct" x="216" y="172">37%</text>
    <circle cx="151" cy="293" r="21" fill="#fff" stroke="#00b1a6" stroke-width="1.5"/>
    <text class="pct" x="151" y="298">58%</text>

    <text x="294" y="122" font-size="12">Text</text>
    <text x="294" y="136" font-size="12">Sample</text>
    <text x="292" y="155" font-size="14" font-weight="700" font-style="italic">Sample</text>
    <text x="286" y="170" font-size="10.5">Sample Text</text>
    <text x="322" y="179" font-size="13">Text</text>
    <text x="292" y="193" font-size="13" font-weight="700">Sample Text</text>
    <text x="294" y="209" font-size="13" font-weight="700" letter-spacing="2">SAMPLE</text>
    <text x="306" y="222" font-size="8.5">SAMPLE</text>

    <text x="245" y="272" font-size="13" font-weight="700">Sample</text>
    <text x="290" y="286" font-size="14">Sample Text</text>
    <text x="296" y="308" font-size="19" font-weight="700" letter-spacing="2.5">SAMPLE TEXT</text>
    <text x="334" y="328" font-size="16">sample Text</text>
    <text x="286" y="351" font-size="20" font-style="italic" letter-spacing="4.5">sample text</text>
  </svg>

  <footer class="slide-footer">
    <span class="footer-brand">Quorv</span>
    <span class="footer-label">| <b>COMPANY</b> PRESENTATION</span>
    <span class="page-number">7</span>
  </footer>
</section>

<section class="slide slide--bullets">
  <header class="slide-header">
    <div class="slide-header__texture" role="img" aria-label="faint diagonal line texture"></div>
    <h1 class="slide-title">JUST TEXT WITH BULLETS</h1>
  </header>

  <ul class="bullet-list">
    <li><b>Aenean</b> ridiculus tortor quis interdum id habitant ad, natoque consectetuer nisl auctor libero quisque euismod ante inceptos malesuada ligula mattis.</li>
    <li><b>Aenean</b> ridiculus tortor quis interdum id habitant ad, natoque consectetuer nisl auctor libero quisque euismod ante inceptos malesuada ligula mattis.</li>
    <li>Nulla, netus pulvinar pellentesque porttitor purus maecenas tellus hac nulla lacus. Lorem. Nostra laoreet nulla, dis cursus nascetur dolor odio Eu Magna molestie montes dui mus cursus habitasse mauris tempor.</li>
    <li>Varius inceptos <b>nascetur</b> mollis dui aptent ultrices. Pretium pulvinar ante lobortis convallis lectus netus vitae penatibus eros at blandit. Parturient.</li>
    <li>Varius inceptos <b>nascetur</b> mollis dui aptent ultrices. Pretium pulvinar ante lobortis convallis lectus netus vitae penatibus eros at blandit. Parturient.</li>
  </ul>

  <footer class="slide-footer">
    <span class="footer-brand">Quorv</span>
    <span class="footer-label">| <b>COMPANY</b> PRESENTATION</span>
    <span class="page-number">8</span>
  </footer>
</section>

<section class="slide slide--cover">
  <div class="cover-texture" role="img" aria-label="subtle diagonal pinstripe texture"></div>
  <h1 class="cover-brand">Quorv</h1>
  <p class="cover-tagline">people in motion</p>
  <dl class="cover-contact">
    <dt>Contact us:</dt>
    <dd>555-010-0147<br><a href="http://www.quorv-example.fr/en">http://www.quorv-example.fr/en</a></dd>
    <dt>Central Office:</dt>
    <dd>Address Line 1<br>Address Line 2</dd>
  </dl>
  <div class="social-links" aria-label="social links">
    <span></span><span></span><span></span><span></span>
  </div>
</section>

</body>
</html>
```